Stand out flyer needed for Boxing gym

Hi we need a trifold brochure designed for our outdoor boxing business it will be delivered to doctors and nutritionists to help their patients be healthier and get fit.We have supplied high res pictures for you to use in the brochure. We need a design that use a lot of yellow so it captures their attention. You can check our website for design colours www.ridgepunch.com.au

Target Market(s)

Overweight or unfit people looking to change their lives

Industry/Entity Type

Health And Wellness

Font styles to use
Sans Serif

Colors
fbee3d
ffffff
000000

Requirements
Must have
• (main heading - large bold font) Get fit lose weight & feel great
• (bold) Unlimited outdoor boxing classes $14.95
• Complete affordability & No judgements guaranteed
• (bold) Tailored programs (bold)
• Our programs are structured so that members of all fitness levels feel confident & comfortable during their start-up phase allowing you to quickly build your fitness
• (bold) Injury prevention (bold)
• Our training systems include techniques that will help you avoid injuries and build balanced strength
• (bold) Strengthen & Tone your core (bold)
• You're core muscles are some of you're most important muscles. Each workout you do incorporates core exercises to help avoid injuries and make you're total body stronger
• (bold) Wake up with more energy(bold)
• Every class you'll do will have you filled with energy the will pump you up for the rest of your day
• (bold) Sleep better(bold)
• One of the best parts of exercise is the benefit it has on your sleeping patterns. You'll sleep deeper & more sound
• (bold) Supportive environment (bold)
• At RIDGE PUNCH you'll be surrounded by trainers & other members who are there to encourage & motivate you to reach your goals and to get you moving more.
• Coupon code: SunRise27

```html
<!DOCTYPE html>
<html lang="en">
<head>
<meta charset="utf-8">
<title>Ridge Punch – Brochure Inner Panels</title>
<link rel="stylesheet" href="https://fonts.googleapis.com/css2?family=Bebas+Neue&family=Mulish:wght@400;700;800&display=swap">
<style>
  :root {
    --yellow: #fbee3d;
    --black: #000000;
    --white: #ffffff;
    --frame: #3d3d3f;
    --ink: #111111;
  }
  * { margin: 0; padding: 0; box-sizing: border-box; }
  html, body { width: 1200px; height: 899px; overflow: hidden; background: var(--frame); }
  body { font-family: "Mulish", Arial, sans-serif; color: var(--ink); }

  .brochure {
    position: absolute; left: 58px; top: 31px;
    width: 1084px; height: 837px;
    background: var(--white); overflow: hidden;
  }
  .photo { position: absolute; top: 0; height: 311px; }
  .photo--gym { left: 0; width: 365px; background: linear-gradient(160deg, #e9e6ea 0%, #b9c2cc 40%, #5d6a80 70%, #2b3446 100%); }
  .photo--stretch { left: 365px; width: 364px; background: linear-gradient(170deg, #d9a94a 0%, #8a8a3c 35%, #4f6f2c 65%, #2f4a1d 100%); }
  .photo--park { left: 729px; width: 355px; background: radial-gradient(circle at 50% 20%, #fff6c8 0%, #c9c27a 25%, #6f8c3a 60%, #3e5e22 100%); }

  .rule-top { position: absolute; left: 0; top: 311px; width: 1084px; height: 8px; background: var(--yellow); }
  .banner { position: absolute; left: 0; top: 318px; width: 1084px; height: 102px; }

  .heading {
    position: absolute; top: 320px; text-align: center;
    font-family: "Bebas Neue", Impact, sans-serif; line-height: 1; font-weight: 400;
  }
  .heading .main { display: block; color: var(--yellow); font-size: 58px; letter-spacing: 0.5px; }
  .heading .sub { display: block; color: var(--white); font-size: 37px; margin-top: -6px; }
  .heading--wake .main { font-size: 46px; }
  .heading--wake .sub { font-size: 36px; margin-top: -4px; }
  .heading--tailored { left: 0; width: 365px; }
  .heading--injury { left: 365px; width: 364px; }
  .heading--wake { left: 729px; width: 355px; }

  .tag-box {
    position: absolute; border: 3px solid var(--black); text-align: center;
    background: var(--white); line-height: 1.05;
  }
  .tag-box .small { display: block; font-size: 22px; }
  .tag-box .big { display: block; font-size: 31px; font-weight: 800; }
  .tag-box--structured { left: 68px; top: 439px; width: 230px; height: 80px; padding-top: 8px; }
  .tag-box--structured .small { font-size: 23px; letter-spacing: 0.3px; }
  .tag-box--structured .big { font-size: 29px; }
  .tag-box--core { left: 432px; top: 579px; width: 230px; height: 81px; padding-top: 7px; }
  .tag-box--sleep { left: 792px; top: 579px; width: 229px; height: 81px; padding-top: 4px; }
  .tag-box--sleep .big { font-size: 37px; line-height: 1; }
  .tag-box--sleep .small { font-size: 29px; line-height: 1; }

  .confidence-panel {
    position: absolute; left: 0; top: 531px; width: 365px; height: 282px;
    background: var(--black); border-radius: 28px 28px 0 0;
    color: var(--white); text-align: center;
    font-size: 30px; line-height: 37.8px; padding-top: 4px; white-space: nowrap;
  }
  .confidence-panel .hl { color: var(--yellow); font-weight: 700; }

  .copy { position: absolute; text-align: center; white-space: nowrap; }
  .copy b { font-weight: 800; }
  .copy--lead { font-size: 23.5px; line-height: 29.7px; top: 437px; }
  .copy--injury { left: 365px; width: 364px; }
  .copy--energy { left: 729px; width: 355px; }
  .copy--core { left: 365px; width: 364px; top: 676px; font-size: 19.7px; line-height: 24.7px; }
  .copy--sleep { left: 729px; width: 355px; top: 693px; font-size: 22.5px; line-height: 28.1px; }

  .rule-bottom { position: absolute; left: 0; top: 813px; width: 1084px; height: 11px; background: var(--yellow); }
  .band-bottom { position: absolute; left: 0; top: 824px; width: 1084px; height: 13px; background: var(--black); }
</style>
</head>
<body>
<main class="brochure">
  <div class="photo photo--gym" role="img" aria-label="Personal trainer with a clipboard standing in a gym"></div>
  <div class="photo photo--stretch" role="img" aria-label="Trainer helping a woman stretch her leg outdoors in a park"></div>
  <div class="photo photo--park" role="img" aria-label="Two people doing planks on the grass in the sunshine"></div>

  <div class="rule-top"></div>
  <svg class="banner" viewBox="0 0 1084 102" aria-hidden="true">
    <polygon points="0,0 365,0 365,51 182.5,102 0,51" fill="#000"/>
    <polygon points="365,0 729,0 729,51 547,102 365,51" fill="#000"/>
    <polygon points="729,0 1084,0 1084,51 906.5,102 729,51" fill="#000"/>
  </svg>

  <h2 class="heading heading--tailored"><span class="main">Tailored</span><span class="sub">Programs</span></h2>
  <h2 class="heading heading--injury"><span class="main">Injury</span><span class="sub">Prevention</span></h2>
  <h2 class="heading heading--wake"><span class="main">Wake up with</span><span class="sub">More Energy</span></h2>

  <div class="tag-box tag-box--structured"><span class="small">Our Programs Are</span><span class="big">STRUCTURED</span></div>
  <p class="confidence-panel">So that members of all<br>fitness levels feel<br><span class="hl">Confident</span> &amp;<br><span class="hl">Comfortable</span> during<br>their start-up phase<br>allowing you to quickly<br>build your <span class="hl">Fitness</span></p>

  <p class="copy copy--lead copy--injury">Our training systems include<br><b>Techniques</b> that will help you<br>avoid injuries and build<br>balanced <b>Strength</b></p>
  <div class="tag-box tag-box--core"><span class="small">Strengthen &amp; Tone</span><span class="big">YOUR CORE</span></div>
  <p class="copy copy--core">Your <b>Core Muscles</b> are some of your<br>most <b>Important Muscles.</b><br>Each workout you do incorporates<br>core exercises to help avoid injuries &amp;<br>make your total <b>Body Stronger</b></p>

  <p class="copy copy--lead copy--energy">Every class you'll do will have<br>you filled with <b>Energy</b> the will<br>pump you up for the rest of<br><b>Your Day</b></p>
  <div class="tag-box tag-box--sleep"><span class="big">SLEEP</span><span class="small">BETTER</span></div>
  <p class="copy copy--sleep">One of the best parts of<br><b>Exercise</b> is the <b>Benefit</b> it has on<br>your <b>Sleeping Patterns</b>. You'll<br>sleep deeper &amp; more sound</p>

  <div class="rule-bottom"></div>
  <div class="band-bottom"></div>
</main>
</body>
</html>
```